Design a Brochure for Tourism

We need a two 2 page brochures. One is in English aimed at English speaking tourists, and the the other in Chinese that is aimed at Chinese tourists. We already have the Chinese translation, we just need the design.

Below is some information to help you:
Website: http://www.doriankestlewayfarings.com/
Text: Headings: Arial Bold, Body: Helvetica Neue or Helvetica (feel free to change it you need)
Here are the colours used on the website, so feel free to use these colours in the design:
Blue Colour Info
Hue: 139
Sat: 175
Lum: 104
Red: 30
Green: 115
Blue: 190

```html
<!DOCTYPE html>
<html lang="en">
<head>
<meta charset="utf-8">
<title>Dorian Kestle Wayfarings — Brochure</title>
<link rel="stylesheet" href="https://fonts.googleapis.com/css2?family=Arimo:wght@400;700&display=swap">
<style>
  :root {
    --brand-blue: #1e73be;
    --panel-blue: #3a9fd1;
    --band-blue: #2f9ad0;
    --band-dark: #3b3d42;
    --paper: #ffffff;
    --paper-soft: #eef0f2;
    --ink: #2a2a2a;
    --ink-soft: #6b6f74;
    --stage: #d9dcdf;
    --map-sea: #a9cbe8;
    --map-land: #e9e4d6;
    --photo-sky: #a8c6e2;
    --photo-grass: #5f9a3a;
  }
  * { box-sizing: border-box; margin: 0; padding: 0; }
  html, body { width: 1200px; height: 847px; overflow: hidden; }
  body { background: var(--stage); font-family: "Arimo", Arial, sans-serif; color: var(--ink); }
  .spread { position: relative; width: 1200px; height: 847px; }
  .page {
    position: absolute; top: 30px; width: 560px; height: 787px;
    background: var(--paper); overflow: hidden;
    box-shadow: 0 6px 18px rgba(0,0,0,.18);
    display: flex; flex-direction: column;
  }
  .page--back { left: 40px; }
  .page--front { left: 600px; }
  .top-band { height: 40px; background: var(--band-dark); flex: none;
    display: flex; align-items: center; justify-content: center;
    color: #d8d8d8; font-size: 11px; letter-spacing: .3px; }

  /* back page */
  .location { display: flex; height: 300px; flex: none; }
  .map { width: 335px; height: 100%; background: linear-gradient(135deg, var(--map-land) 0%, var(--map-land) 55%, var(--map-sea) 85%); }
  .location-panel { flex: 1; background: var(--panel-blue); padding: 22px 20px; color: #fff; }
  .location-panel h2 { font-weight: 700; font-size: 30px; margin-bottom: 10px; }
  .location-panel p { font-size: 14px; line-height: 1.45; text-align: justify; }
  .soft-band { flex: 1; background: linear-gradient(180deg, var(--paper-soft), var(--paper)); display: flex; align-items: center; padding-left: 70px; }
  .contact-band { height: 185px; flex: none; background: var(--band-blue); padding: 80px 0 0 80px; color: #fff; font-size: 15px; font-weight: 700; }
  .contact-line { display: flex; align-items: center; gap: 8px; margin-bottom: 8px; }

  /* brand mark */
  .brand { display: flex; align-items: center; gap: 14px; }
  .brand-dot { width: 34px; height: 34px; border-radius: 50%; border: 2px solid var(--ink-soft); flex: none; }
  .brand-name { font-size: 14px; font-weight: 400; color: var(--ink); }
  .brand-tagline { font-size: 12px; color: var(--ink-soft); margin-left: 40px; font-style: italic; }

  /* front page */
  .hero { position: relative; height: 260px; flex: none; background: linear-gradient(180deg, var(--photo-sky) 0%, #c9d9c0 55%, var(--photo-grass) 70%, #4f8a30 100%); }
  .hero-title { position: absolute; left: 70px; bottom: 30px; font-size: 34px; font-weight: 700; line-height: 1; color: var(--brand-blue); text-transform: uppercase; }
  .front-logo { height: 150px; flex: none; background: var(--paper); border-top: 3px solid var(--band-dark); display: flex; align-items: center; padding-left: 60px; }
  .intro-band { flex: 1; background: var(--band-blue); color: #fff; padding: 30px 30px 0 70px; }
  .intro-band h3 { font-size: 19px; font-weight: 700; margin-bottom: 14px; }
  .intro-band p { font-size: 15px; line-height: 1.4; }
</style>
</head>
<body>
<main class="spread">
  <section class="page page--back">
    <div class="top-band"></div>
    <div class="location">
      <div class="map" role="img" aria-label="Road map showing the driving route from Sydney to the Brookvale Ridge facility"></div>
      <div class="location-panel">
        <h2>Location</h2>
        <p>Located just 20 minutes from Sydney, Brookvale Ridge is a pristine equestrian facility where training practices are based on understanding and communicating with horses to achieve the best possible outcomes.</p>
      </div>
    </div>
    <div class="soft-band">
      <div>
        <div class="brand"><span class="brand-dot"></span><span class="brand-name">Dorian Kestle Wayfarings</span></div>
        <div class="brand-tagline">think outside the square</div>
      </div>
    </div>
    <div class="contact-band">
      <div class="contact-line">
        <svg width="14" height="14" viewBox="0 0 24 24" aria-hidden="true"><path fill="#fff" d="M6.6 10.8a15 15 0 0 0 6.6 6.6l2.2-2.2c.3-.3.7-.4 1-.2 1.1.4 2.3.6 3.6.6.6 0 1 .4 1 1V20c0 .6-.4 1-1 1A17 17 0 0 1 3 4c0-.6.4-1 1-1h3.5c.6 0 1 .4 1 1 0 1.3.2 2.5.6 3.6.1.3 0 .7-.2 1z"/></svg>
        <span>0487 530 164</span>
      </div>
      <div class="contact-line">
        <svg width="14" height="12" viewBox="0 0 24 20" aria-hidden="true"><rect x="1" y="1" width="22" height="18" fill="none" stroke="#fff" stroke-width="2"/><path d="M1 1l11 9 11-9" fill="none" stroke="#fff" stroke-width="2"/></svg>
        <span>info@doriankestlewayfarings.com</span>
      </div>
    </div>
  </section>

  <section class="page page--front">
    <div class="top-band">www.doriankestlewayfarings.com</div>
    <div class="hero" role="img" aria-label="Photo of a timber stable barn on a green lawn surrounded by trees">
      <div class="hero-title">Connecting with<br>horses</div>
    </div>
    <div class="front-logo">
      <div>
        <div class="brand"><span class="brand-dot"></span><span class="brand-name">Dorian Kestle Wayfarings</span></div>
        <div class="brand-tagline">think outside the square</div>
      </div>
    </div>
    <div class="intro-band">
      <h3>Learn the secret language of the horse</h3>
      <p>We are offering a unique and amazing experience! You will visit and be hands-on with horses in a way you have never seen before!</p>
    </div>
  </section>
</main>
</body>
</html>
```